Business Card Design Project

"Crestline Record Services" is database management company working in the direct marketing & digital printing industries. Currently going through a name & rebranding process we require a new company business card.

Industry/Entity Type

Marketing

```html
<!DOCTYPE html>
<html lang="en">
<head>
<meta charset="utf-8">
<title>Crestline Record Services – Business Card</title>
<link rel="stylesheet" href="https://fonts.googleapis.com/css2?family=Arimo:wght@400;700&display=swap">
<style>
  :root {
    --stage: #ececec;
    --blue-light: #3bb6f0;
    --blue-mid: #1a9ce0;
    --blue-deep: #0a78c4;
    --blue-ring: #12a4ec;
    --paper: #f4f5f6;
    --band: #5c626c;
    --ink: #3b424d;
    --ink-dark: #1f2329;
    --white: #ffffff;
  }
  * { margin: 0; padding: 0; box-sizing: border-box; }
  html, body {
    width: 1155px; height: 1200px; overflow: hidden;
    background: var(--stage);
    font-family: "Arimo", Arial, sans-serif;
  }
  .card {
    position: absolute; left: 168px;
    width: 819px; height: 466px;
    border-radius: 16px; overflow: hidden;
    box-shadow: 0 4px 14px rgba(0,0,0,0.18);
  }
  .card-front { top: 115px; }
  .card-back { top: 619px; }
  .card-art { position: absolute; inset: 0; }

  .name-band {
    position: absolute; left: 8px; top: 98px;
    width: 386px; height: 112px;
    background: var(--band);
    box-shadow: 0 3px 6px rgba(0,0,0,0.25);
    color: var(--white);
    padding: 13px 0 0 44px;
  }
  .person-name { font-size: 38px; font-weight: 700; line-height: 44px; }
  .person-title { font-size: 27px; font-weight: 400; line-height: 36px; }

  .address {
    position: absolute; left: 51px; top: 226px;
    color: var(--white); font-size: 19px; font-weight: 700; line-height: 29px;
  }
  .contacts {
    position: absolute; left: 51px; top: 296px;
    list-style: none; color: var(--white); font-size: 19px; line-height: 28px;
  }
  .contacts li { display: flex; align-items: center; }
  .contacts svg { width: 22px; height: 20px; margin-right: 11px; fill: var(--white); }

  .wordmark {
    position: absolute; font-weight: 700; text-align: center;
    letter-spacing: 0.5px;
  }
  .wordmark-front {
    left: 404px; top: 166px; width: 390px;
    font-size: 40px; line-height: 50px; color: var(--ink);
  }
  .wordmark-back {
    left: 160px; top: 168px; width: 500px;
    font-size: 50px; line-height: 60px; color: var(--white);
  }
  .website {
    position: absolute; left: 0; right: 0; top: 422px;
    text-align: center; font-size: 24px; color: var(--ink-dark);
  }
</style>
</head>
<body>

<section class="card card-front" aria-label="Business card front">
  <svg class="card-art" viewBox="0 0 819 466" aria-hidden="true">
    <defs>
      <linearGradient id="frontBlue" x1="0" y1="0" x2="1" y2="0">
        <stop offset="0" stop-color="var(--blue-light)"/>
        <stop offset="1" stop-color="var(--blue-mid)"/>
      </linearGradient>
    </defs>
    <rect width="819" height="466" fill="url(#frontBlue)"/>
    <circle cx="738" cy="233" r="366" fill="var(--blue-ring)"/>
    <circle cx="738" cy="233" r="352" fill="var(--paper)"/>
  </svg>

  <div class="name-band">
    <p class="person-name">Dana Royce</p>
    <p class="person-title">Sales Manager</p>
  </div>

  <p class="address">412 Harwick Blvd.<br>Unit 7 Milton, Ontario L9T 2X5</p>

  <ul class="contacts">
    <li><svg viewBox="0 0 22 20"><path d="M2 7c0-3 4-5 9-5s9 2 9 5v2h-5V7H7v2H2z"/><path d="M5 10h12l2 8H3z"/></svg>905.555.0148 x 223</li>
    <li><svg viewBox="0 0 22 20"><rect x="6" y="1" width="10" height="6"/><rect x="2" y="8" width="18" height="8" rx="1"/><rect x="6" y="13" width="10" height="6" fill="var(--blue-mid)" stroke="#fff" stroke-width="1.5"/></svg>905.555.0172</li>
    <li><svg viewBox="0 0 22 20"><rect x="7" y="1" width="9" height="18" rx="1.5" fill="none" stroke="#fff" stroke-width="2"/><rect x="9" y="4" width="5" height="8"/></svg>416.555.0193</li>
    <li><svg viewBox="0 0 22 20"><rect x="2" y="4" width="18" height="12" fill="none" stroke="#fff" stroke-width="2"/><path d="M2 4l9 7 9-7" fill="none" stroke="#fff" stroke-width="2"/></svg>drayce@crestlinerecords.com</li>
  </ul>

  <p class="wordmark wordmark-front">Crestline<br>Record Services</p>
</section>

<section class="card card-back" aria-label="Business card back">
  <svg class="card-art" viewBox="0 0 819 466" aria-hidden="true">
    <defs>
      <linearGradient id="backBlue" x1="0" y1="0" x2="1" y2="0">
        <stop offset="0" stop-color="var(--blue-light)"/>
        <stop offset="1" stop-color="var(--blue-deep)"/>
      </linearGradient>
    </defs>
    <rect width="819" height="466" fill="var(--paper)"/>
    <path d="M0 0H819V338Q410 258 0 330Z" fill="var(--blue-ring)"/>
    <path d="M0 0H819V328Q410 248 0 318Z" fill="url(#backBlue)"/>
  </svg>

  <p class="wordmark wordmark-back">Crestline<br>Record Services</p>

  <p class="website">www.crestlinerecords.com</p>
</section>

</body>
</html>
```